IT Consulting Business Card Design

We need a business card on our company name....which is a IT consulting and staffing company. We also train masters graduates in various IT courses. 70% of the time these cards will be handed out to the graduate students at the universities. 30% for our clients and business partners. We are uploading our company logo...would like to see something that matches our logo or blends with it. Please visit www.brightvaleworks.com for more details on logo and colors.

Target Market(s)

70% of the time these cards will be handed out to the graduate students at the universities. 30% for our clients and business partners.

Industry/Entity Type

Business

Contact Information for Business Card

Ravi Kondamuri
Vice-President
Bright Vale Works Inc
3807 Morrow Lane, Suite 412
East Brookridge, NJ 07315
ravi@brightvaleworks.com
Office : 1-866-219-3840 X 515
Cell number : 732-581-9034

Requirements
Nice to have
• may be company logo and name on the back of the card and detials on the other side...just a thought..!!

```html
<!DOCTYPE html>
<html lang="en">
<head>
<meta charset="utf-8">
<title>Bright Vale Works – Business Card</title>
<link rel="stylesheet" href="https://fonts.googleapis.com/css2?family=Arimo:wght@400&family=Noto+Sans:wght@400;700&display=swap">
<style>
  :root {
    --steel-light: #d3d7db;
    --steel-mid: #b9bec3;
    --band: #a9aeb3;
    --charcoal: #3a3a3b;
    --charcoal-deep: #2f2f30;
    --brand-red: #e02228;
    --ink: #333335;
    --panel: rgba(150, 150, 150, 0.45);
    --panel-text: #ececec;
    --white: #ffffff;
  }
  html, body {
    margin: 0;
    padding: 0;
    width: 1025px;
    height: 1200px;
    overflow: hidden;
    background: #ffffff;
  }
  .card {
    position: relative;
    width: 1025px;
    height: 1200px;
    overflow: hidden;
    font-family: "Noto Sans", sans-serif;
  }
  .brand-area {
    position: absolute;
    left: 0; top: 0;
    width: 1025px; height: 428px;
    background:
      repeating-linear-gradient(45deg, rgba(255,255,255,0.05) 0 2px, rgba(0,0,0,0.03) 2px 4px),
      radial-gradient(ellipse at 50% 40%, #dde1e5 0%, var(--steel-light) 45%, var(--steel-mid) 100%);
  }
  .brand-mark {
    position: absolute;
    left: 140px; top: 122px;
    width: 180px; height: 180px;
    border-radius: 50%;
    background: var(--brand-red);
  }
  .brand-name {
    position: absolute;
    left: 350px; top: 186px;
    margin: 0;
    font-family: "Noto Sans", sans-serif;
    font-weight: 700;
    font-size: 50px;
    line-height: 60px;
    letter-spacing: -0.5px;
    color: var(--ink);
    white-space: nowrap;
  }
  .address-band {
    position: absolute;
    left: 0; top: 428px;
    width: 1025px; height: 170px;
    background: linear-gradient(180deg, #9fa4a9 0%, var(--band) 6%, #b4b9be 100%);
    box-shadow: inset 0 2px 3px rgba(0,0,0,0.2);
    color: var(--ink);
    text-align: center;
  }
  .address-band p { margin: 0; white-space: nowrap; }
  .address-line {
    font-size: 32px;
    line-height: 36px;
    letter-spacing: 0.3px;
  }
  .address-line.first { padding-top: 8px; }
  .website {
    font-size: 36px;
    line-height: 46px;
    margin-left: -30px !important;
  }
  .contact-side {
    position: absolute;
    left: 0; top: 598px;
    width: 1025px; height: 602px;
    background:
      repeating-linear-gradient(45deg, rgba(255,255,255,0.025) 0 2px, rgba(0,0,0,0.05) 2px 4px),
      linear-gradient(180deg, var(--charcoal) 0%, var(--charcoal-deep) 100%);
  }
  .name-plate {
    position: absolute;
    left: 408px; top: 3px;
    width: 617px; height: 188px;
    background: var(--brand-red);
    box-shadow: -2px 3px 6px rgba(0,0,0,0.45);
    color: var(--white);
    font-family: "Arimo", sans-serif;
    text-align: right;
  }
  .person-name {
    margin: 0;
    padding: 60px 36px 0 0;
    font-size: 59px;
    line-height: 60px;
    font-weight: 400;
    word-spacing: 8px;
    white-space: nowrap;
  }
  .person-title {
    margin: 0;
    padding-right: 36px;
    font-size: 38px;
    line-height: 50px;
    font-weight: 400;
  }
  .contact-panel {
    position: absolute;
    left: 408px; top: 344px;
    width: 617px; height: 184px;
    background: var(--panel);
    color: var(--panel-text);
    font-size: 34px;
    letter-spacing: 1px;
  }
  .contact-panel ul {
    list-style: none;
    margin: 0;
    padding: 16px 0 0 38px;
  }
  .contact-panel li {
    line-height: 53px;
    white-space: nowrap;
  }
  .contact-label { display: inline-block; min-width: 40px; }
  .contact-label.cell { min-width: 72px; }
</style>
</head>
<body>
<main class="card">
  <section class="brand-area">
    <div class="brand-mark"></div>
    <h1 class="brand-name">BRIGHT VALE WORKS</h1>
  </section>

  <section class="address-band">
    <p class="address-line first">3807 Morrow Lane, Suite 412</p>
    <p class="address-line">East Brookridge, NJ 07315</p>
    <p class="website">www.BrightValeWorks.com</p>
  </section>

  <section class="contact-side">
    <div class="name-plate">
      <h2 class="person-name">RAVI KONDAMURI</h2>
      <p class="person-title">VICE-PRESIDENT</p>
    </div>
    <div class="contact-panel">
      <ul>
        <li><span class="contact-label">P:</span> 1-866-219-3840 (x.515)</li>
        <li><span class="contact-label cell">C:</span> 732-581-9034</li>
        <li><span class="contact-label">E:</span> ravi@brightvaleworks.com</li>
      </ul>
    </div>
  </section>
</main>
</body>
</html>
```